Varlow Industries Luxury Candles

Luxury box design,, simple and sophisticated look,,

My collection of candles come in 5 different fragrances, i would like to be able to change the fragrance name on the boxes,,,,

I would like the outline of australia on the front down the bottom , (only small) to represent this is an australian product.

My boxes are white gloss,,,

Happy for you to use my current logo ,,, however you'll have to change Varlow Nails to Varlow Industries.

```html
<!DOCTYPE html>
<html lang="en">
<head>
<meta charset="utf-8">
<title>Varlow Industries Luxury Candles – Box Panels</title>
<link rel="stylesheet" href="https://fonts.googleapis.com/css2?family=Cormorant+Garamond:ital,wght@0,400;0,500;1,400&display=swap">
<style>
  :root {
    --page: #ffffff;
    --frame: #e4e0cc;
    --card: #ffffff;
    --ink: #1f1f1c;
    --green-deep: #4a6b55;
    --green-mid: #6f8f7c;
    --teal-soft: #9fb5ae;
    --umber: #5b4f48;
    --sand: #c9bd8f;
    --cream: #f1eedf;
    --badge: #c9ccca;
  }
  * { box-sizing: border-box; margin: 0; padding: 0; }
  html, body {
    width: 1200px; height: 842px; overflow: hidden;
    background: var(--page);
  }
  .sheet { position: relative; width: 1200px; height: 842px; }

  .box-panel {
    position: absolute; top: 88px;
    width: 454px; height: 670px;
    overflow: hidden;
  }
  .box-panel--front { left: 109px; }
  .box-panel--back { left: 638px; }

  .wash {
    position: absolute; inset: 0;
    background:
      radial-gradient(ellipse 180px 140px at 18% 88%, rgba(91,79,72,0.75), transparent 70%),
      radial-gradient(ellipse 220px 160px at 15% 20%, rgba(74,107,85,0.55), transparent 70%),
      linear-gradient(125deg,
        var(--green-mid) 0%,
        var(--teal-soft) 22%,
        var(--green-deep) 40%,
        var(--teal-soft) 55%,
        var(--green-mid) 62%,
        #dfe3dc 70%,
        var(--sand) 80%,
        var(--cream) 90%,
        #faf9f3 100%);
  }

  .label-card {
    position: absolute; left: 69px; top: 135px;
    width: 332px; height: 331px;
    background: var(--card);
    border: 6px solid var(--frame);
    text-align: center;
    color: var(--ink);
    font-family: "Cormorant Garamond", serif;
  }

  .brand-name {
    position: absolute; left: 0; right: 0;
    font-weight: 500; letter-spacing: 0.5px;
  }
  .brand-tagline {
    position: absolute; left: 0; right: 0;
    text-transform: uppercase; font-weight: 400;
  }

  .box-panel--front .brand-name { top: 50px; font-size: 36px; }
  .box-panel--front .brand-tagline { top: 104px; font-size: 14px; letter-spacing: 4px; }
  .fragrance-name {
    position: absolute; left: 0; right: 0; top: 275px;
    font-size: 14px; letter-spacing: 4.5px; text-transform: uppercase;
  }

  .box-panel--back .brand-name { top: 40px; font-size: 22px; }
  .box-panel--back .brand-tagline { top: 71px; font-size: 8px; letter-spacing: 2.5px; }
  .product-description {
    position: absolute; left: 35px; right: 35px; top: 94px;
    font-size: 11.5px; font-style: italic; line-height: 25px;
  }

  .origin-badge {
    position: absolute; left: 31px; top: 605px;
    width: 46px; height: 41px;
    background: var(--badge);
    border-radius: 6px;
  }
</style>
</head>
<body>
<main class="sheet">

  <section class="box-panel box-panel--front">
    <div class="wash" role="img" aria-label="Abstract watercolour wash in sage green, teal, umber and sand tones"></div>
    <div class="label-card">
      <h1 class="brand-name">Varlow Industries</h1>
      <p class="brand-tagline">Luxury Candles</p>
      <p class="fragrance-name">Vanilla Caramel</p>
    </div>
    <div class="origin-badge" role="img" aria-label="Small outline of Australia marking an Australian product"></div>
  </section>

  <section class="box-panel box-panel--back">
    <div class="wash" role="img" aria-label="Abstract watercolour wash in sage green, teal, umber and sand tones"></div>
    <div class="label-card">
      <h2 class="brand-name">Varlow Industries</h2>
      <p class="brand-tagline">Luxury Candles</p>
      <p class="product-description">orem ipsum dolor sit amet, consectetur adipiscing elit. Vestibulum efficitur lobortis orci ac consequat. Ut porta pellentesque metus, sit amet tristique turpis ornare in. Ut dignissim ligula nisi, vitae mollis lacus mollis semper. Nulla tincidunt porttitor nisi eget luctus. Vestibulum efficitur fringilla enim id vehicula. Proin suscipit, diam nec bibendum ullamcorper, odio quam gravida libero, vel tristique nisi turpis id purus. Phasellus ac tincidunt magna. Sed scelerisque interdum magna ut tempor.</p>
    </div>
  </section>

</main>
</body>
</html>
```